Breezeway Comfort business cards design

Need a business card design for a Heating and Air Conditioning business. I need these items included.
Business name: Breezeway Comfort
Owner: Marcus Tollefsen
License # 2874590
Phone number # 555-382-4071
Email: breezewaycomfortair@mailvista.example
Sales
Service
Installation
Maintenance

Heating and Air Conditioning

Requirements
Must have
• Company name , license number , phone number , email

```html
<!DOCTYPE html>
<html lang="en">
<head>
<meta charset="utf-8">
<title>Breezeway Comfort – Business Cards</title>
<link href="https://fonts.googleapis.com/css2?family=Poppins:wght@400;500;600;700&display=swap" rel="stylesheet">
<style>
  :root {
    --stage: #2b2c30;
    --brand-blue: #1f48a8;
    --brand-blue-deep: #1a3d99;
    --brand-cyan: #13a6dc;
    --brand-orange: #f47a2a;
    --brand-orange-light: #f7a031;
    --paper: #ffffff;
  }
  * { box-sizing: border-box; margin: 0; padding: 0; }
  html, body {
    width: 1200px; height: 900px; overflow: hidden;
    background: var(--stage);
    font-family: "Poppins", sans-serif;
  }
  .canvas { position: relative; width: 1200px; height: 900px; }

  .card {
    position: absolute; left: 250px;
    width: 700px; height: 400px;
    border-radius: 22px; overflow: hidden;
  }

  /* Logo-side card */
  .card--brand {
    top: 30px;
    background: radial-gradient(ellipse 60% 70% at 50% 45%, var(--brand-cyan) 0%, #1770c8 45%, var(--brand-blue) 85%);
  }
  .brand-name {
    position: absolute; top: 130px; left: 0; width: 100%;
    text-align: center;
    font-weight: 600; font-size: 54px; letter-spacing: 1px;
    color: var(--paper);
  }
  .brand-name .mark-dot {
    display: inline-block; width: 30px; height: 30px; border-radius: 50%;
    background: var(--paper); margin-right: 16px; vertical-align: 2px;
  }
  .services {
    position: absolute; bottom: 48px; left: 0; width: 100%;
    display: flex; justify-content: center; align-items: center; gap: 22px;
    color: var(--paper); font-size: 15px; font-weight: 500; letter-spacing: 1.5px;
    text-transform: uppercase;
  }
  .services .sep {
    width: 8px; height: 8px; border-radius: 50%; background: var(--brand-orange);
  }

  /* Contact card */
  .card--contact { top: 470px; background: var(--paper); }
  .card--contact .wave { position: absolute; inset: 0; }
  .contact-brand {
    position: absolute; top: 56px; left: 50px;
    font-weight: 600; font-size: 32px; color: var(--brand-blue-deep);
    white-space: nowrap;
  }
  .contact-brand .mark-dot {
    display: inline-block; width: 20px; height: 20px; border-radius: 50%;
    background: var(--brand-blue-deep); margin-right: 10px; vertical-align: 2px;
  }
  .contact-info {
    position: absolute; right: 28px; top: 160px;
    text-align: right; color: var(--paper);
    white-space: nowrap;
  }
  .contact-info .person { font-size: 26px; font-weight: 700; color: var(--brand-orange); line-height: 1.1; }
  .contact-info .role { font-size: 14px; margin-bottom: 8px; }
  .contact-info .license { font-size: 15px; margin-bottom: 8px; }
  .contact-info .license span { color: var(--brand-orange); }
  .contact-info .line { font-size: 14px; display: flex; justify-content: flex-end; align-items: center; gap: 10px; margin-bottom: 6px; }
  .contact-info .icon {
    width: 22px; height: 22px; border-radius: 4px; background: var(--brand-orange);
    display: inline-flex; align-items: center; justify-content: center;
  }
</style>
</head>
<body>
<div class="canvas">

  <section class="card card--brand">
    <div class="brand-name"><span class="mark-dot"></span>Breezeway Comfort</div>
    <div class="services">
      <span>Sales</span><span class="sep"></span>
      <span>Service</span><span class="sep"></span>
      <span>Installation</span><span class="sep"></span>
      <span>Maintenance</span>
    </div>
  </section>

  <section class="card card--contact">
    <svg class="wave" viewBox="0 0 700 400" width="700" height="400" aria-hidden="true">
      <defs>
        <linearGradient id="waveOrange" x1="0" y1="1" x2="1" y2="0">
          <stop offset="0" stop-color="var(--brand-orange-light)"/>
          <stop offset="1" stop-color="var(--brand-orange)"/>
        </linearGradient>
        <linearGradient id="waveBlue" x1="0" y1="1" x2="1" y2="0">
          <stop offset="0" stop-color="var(--brand-blue)"/>
          <stop offset="0.5" stop-color="var(--brand-cyan)"/>
          <stop offset="1" stop-color="var(--brand-blue)"/>
        </linearGradient>
      </defs>
      <path d="M605,0 C490,70 410,160 340,240 C270,320 170,382 0,392 L0,400 L700,400 L700,0 Z" fill="url(#waveOrange)"/>
      <path d="M640,0 C520,70 440,160 370,240 C300,320 190,385 0,400 L700,400 L700,0 Z" fill="url(#waveBlue)" stroke="#ffffff" stroke-width="6"/>
    </svg>

    <div class="contact-brand"><span class="mark-dot"></span>Breezeway Comfort</div>

    <div class="contact-info">
      <div class="person">Marcus Tollefsen</div>
      <div class="role">Owner</div>
      <div class="license"><span>License #</span> 2874590</div>
      <div class="line">555-382-4071
        <span class="icon"><svg width="13" height="13" viewBox="0 0 24 24"><path fill="#fff" d="M6.6 10.8a15 15 0 0 0 6.6 6.6l2.2-2.2a1 1 0 0 1 1-.25 11.4 11.4 0 0 0 3.6.6 1 1 0 0 1 1 1V20a1 1 0 0 1-1 1A17 17 0 0 1 3 4a1 1 0 0 1 1-1h3.5a1 1 0 0 1 1 1c0 1.25.2 2.45.6 3.6a1 1 0 0 1-.25 1z"/></svg></span>
      </div>
      <div class="line">breezewaycomfortair@mailvista.example
        <span class="icon"><svg width="13" height="13" viewBox="0 0 24 24"><rect x="2" y="5" width="20" height="14" rx="2" fill="#fff"/><path d="M3 6l9 7 9-7" fill="none" stroke="#f47a2a" stroke-width="2"/></svg></span>
      </div>
    </div>
  </section>

</div>
</body>
</html>
```